Atelier Marrow Architecture business card

We need to update our business card. We do high end custom residential, hospitality, and wellness architecture. We focus on creating unique spaces and design around the five senses, believing that architecture's true impact is not on our surroundings, but within us. We would like to see designs are instill a sense of calm awe. They should be crisp, fresh, clean, authentic, & contemporary without being sterile, overworked, or harsh. White space is important. Alternative materials are an option if natural. We have created our own logo and would like designs to incorporate it. However, we are willing to see alternatives if the logo becomes a stumbling block and you have an alternate you suggest. Card must have the following information:
Atelier Marrow Architecture, Inc.
728 Holloway Ct. NE Atlanta, GA 30318
Marcus T. Whitcombe, AIA, NCARB, LEED AP BD+C
ateliermarrow.example

Target Market(s)

Higher net worth individuals with an appreciation for design, nature, sustainability,

Industry/Entity Type

Architect

Contact Information for Business Card

See above. The title of Owner or Architect is helpful but not necessary. Minimalism should trump additional information.

Font styles to use
Serif
Sans Serif

Requirements
Must have
• It should look professional. It must use logo
Should not have
• caligraphy, animals, anything that is cute,

```html
<!DOCTYPE html>
<html lang="en">
<head>
<meta charset="utf-8">
<title>Atelier Marrow Architecture — Business Card</title>
<link rel="stylesheet" href="https://fonts.googleapis.com/css2?family=Source+Sans+3:wght@400&display=swap">
<style>
  :root {
    --backdrop: #1f1b1a;
    --card: #ffffff;
    --ink: #1e1e1e;
    --ink-soft: #333333;
    --forest: #0f5a3e;
    --brush-green: #12641a;
    --mark-grey: #4a4a4a;
  }
  * { margin: 0; padding: 0; box-sizing: border-box; }
  html, body {
    width: 1200px; height: 900px; overflow: hidden;
    background: var(--backdrop);
    font-family: "Source Sans 3", "Helvetica Neue", Arial, sans-serif;
  }
  .canvas { position: relative; width: 1200px; height: 900px; }
  .card {
    position: absolute;
    width: 716px; height: 418px;
    background: var(--card);
  }
  .card--front { left: 100px; top: 28px; text-align: center; color: var(--ink); }
  .card--back { left: 384px; top: 456px; }

  .holder-name { position: absolute; top: 52px; width: 100%; font-size: 26px; color: var(--forest); }
  .holder-credentials { position: absolute; top: 90px; width: 100%; font-size: 15px; color: var(--ink-soft); }
  .wordmark {
    position: absolute; top: 176px; width: 100%;
    font-size: 30px; letter-spacing: 0.22em; text-transform: uppercase;
    color: var(--mark-grey);
  }
  .firm-name { position: absolute; top: 296px; width: 100%; font-size: 25px; }
  .firm-address { position: absolute; top: 336px; width: 100%; font-size: 18px; }
  .firm-web { position: absolute; top: 366px; width: 100%; font-size: 18px; }

  .brush-field {
    position: absolute; left: 160px; top: 100px;
    width: 200px; height: 190px;
    background: var(--brush-green);
    border-radius: 40px 90px 30px 60px;
  }
  .wordmark--back {
    top: auto; left: 380px; width: auto; top: 172px;
    font-size: 26px; letter-spacing: 0.2em; text-align: left;
    line-height: 1.25;
  }
</style>
</head>
<body>
<main class="canvas">
  <section class="card card--front" aria-label="Card front">
    <h1 class="holder-name">Marcus T. Whitcombe</h1>
    <p class="holder-credentials">AIA, NCARB, LEED AP BD+C</p>
    <p class="wordmark">Atelier Marrow Architecture</p>
    <p class="firm-name">Atelier Marrow Architecture, Inc.</p>
    <p class="firm-address">728 Holloway Ct. NE Atlanta, GA 30318</p>
    <p class="firm-web">ateliermarrow.example</p>
  </section>

  <section class="card card--back" aria-label="Card back">
    <div class="brush-field" role="img" aria-label="Loose green brushstroke texture"></div>
    <p class="wordmark wordmark--back">Atelier Marrow<br>Architecture</p>
  </section>
</main>
</body>
</html>
```